Need a design for Loan Site with new age design

We need a design for our site www.credvista.in , we deal with different verticals like home loan, personal loan, loan against property and business loans. Feel free to get in touch if you have any questions.

I have like the concept of the drop down on the eye level where consumer is able to select the product they wish and continue with the form https://www.tulsiorbit.com/ . They are in the same line of business as we are.

Here are few more designs which i personally like just to get idea about the taste

https://plumridgestudio.com/
http://zenpik.com/partners

Industry/Entity Type

Loan

Number of Pages Required

2 page

Colors
34a7d7
add136
faa54b
fbee3e

Requirements
Must have
• I have like the concept of the drop down on the eye level where consumer is able to select the product they wish and continue with the form https://www.tulsiorbit.com/ . They are in the same line of business as we are.
• Here are few more designs which i personally like just to get idea about the taste
• https://plumridgestudio.com/
• http://zenpik.com/partners

```html
<!DOCTYPE html>
<html lang="en">
<head>
<meta charset="utf-8">
<title>CredVista – Secured &amp; Unsecured Business Loans</title>
<link href="https://fonts.googleapis.com/css2?family=Montserrat:wght@400;500;600;700&family=Open+Sans:wght@400;600&display=swap" rel="stylesheet">
<style>
  :root{
    --sky:#36a8da;
    --navy:#17599a;
    --deep:#0b2f5c;
    --lime:#add136;
    --ink:#1f1f1f;
    --muted:#6b6b6b;
    --line:#ececec;
    --foot:#f1f1f1;
    --white:#ffffff;
  }
  *{box-sizing:border-box;margin:0;padding:0}
  html,body{width:1152px;height:1200px;overflow:hidden;background:var(--white)}
  body{font-family:"Montserrat",sans-serif;color:var(--ink);position:relative}

  .topbar{position:absolute;left:0;top:0;width:1152px;height:29px;background:var(--sky);color:var(--white);font-size:7.5px;font-weight:700;letter-spacing:.1px}
  .topbar .left{position:absolute;left:234px;top:10px;display:flex;align-items:center;gap:6px}
  .topbar .right{position:absolute;right:234px;top:10px;display:flex;align-items:center;gap:6px}
  .topbar .soft{font-weight:600;opacity:.85}

  .header{position:absolute;left:0;top:29px;width:1152px;height:66px;border-bottom:1px solid var(--line)}
  .brand{position:absolute;left:234px;top:22px;display:flex;align-items:center;gap:7px;font-size:17px;font-weight:700;color:var(--navy)}
  .brand .mark{width:14px;height:14px;background:var(--sky)}
  .nav{position:absolute;right:234px;top:28px;display:flex;gap:25px;font-size:8.5px;font-weight:500;letter-spacing:.2px}

  .hero{position:absolute;left:0;top:95px;width:1152px;height:300px;overflow:hidden;background:linear-gradient(90deg,#f2f2f2 0,#e9e9e9 12%,#dedede 40%,#e4e4e4 70%,#ececec 100%)}
  .hero .person{position:absolute;left:212px;top:0;width:264px;height:300px;background:linear-gradient(180deg,#8a7a70 0,#5c5d62 45%,#3e4046 100%);border-radius:120px 120px 0 0}
  .hero h1{position:absolute;left:0;width:1152px;top:42px;text-align:center;font-size:35px;line-height:34.5px;font-weight:700;color:#1c1c1c;letter-spacing:.6px}
  .hero .tag{position:absolute;left:443px;top:163px;width:266px;height:21px;background:var(--sky);color:var(--white);font-size:10px;font-weight:700;text-align:center;line-height:21px;letter-spacing:.2px}
  .search{position:absolute;left:394px;top:221px;height:31px;display:flex;font-family:"Open Sans",sans-serif}
  .select{width:121px;height:31px;background:var(--white);border-right:1px solid var(--line);font-size:8px;color:#555;display:flex;align-items:center;justify-content:space-between;padding:0 11px 0 12px}
  .btn-search{width:120px;height:31px;background:var(--lime);color:var(--white);font-family:"Montserrat",sans-serif;font-weight:700;font-size:10px;letter-spacing:.5px;display:flex;align-items:center;justify-content:center;gap:20px}

  .features{position:absolute;left:0;top:395px;width:1152px}
  .section-title{text-align:center;color:var(--navy);font-weight:700;font-size:17.5px;letter-spacing:.3px}
  .features .section-title{position:absolute;top:33px;width:100%}
  .cards{position:absolute;left:234px;top:80px;display:flex}
  .card{width:171px;height:171px;border-right:1px solid var(--line);display:flex;flex-direction:column;align-items:center;text-align:center;font-size:11px;line-height:14.5px;font-weight:500;color:#222;padding-top:34px}
  .card svg{margin-bottom:auto}
  .card p{margin-bottom:auto}
  .card.active{background:var(--sky);color:var(--white);border-right-color:var(--sky)}
  .cards .card:last-child{border-right:1px solid #f4f4f4}

  .cta{position:absolute;left:0;top:690px;width:1152px;height:240px;background:linear-gradient(180deg,#0a2a52 0,#0d3567 55%,#124179 100%)}
  .cta h2{position:absolute;top:56px;width:100%;text-align:center;color:var(--white);font-size:37px;font-weight:700;letter-spacing:.6px}
  .btn-inquire{position:absolute;left:502px;top:151px;width:149px;height:29px;background:var(--lime);color:var(--white);font-size:10.5px;font-weight:700;letter-spacing:.3px;display:flex;align-items:center;justify-content:center;gap:10px}

  .partners{position:absolute;left:0;top:930px;width:1152px;height:170px}
  .partners .section-title{position:absolute;top:43px;width:100%}
  .logos{position:absolute;top:102px;left:0;width:100%;display:flex;justify-content:center;gap:38px;font-size:14px;font-weight:700}
  .logos span{display:flex;align-items:center;gap:5px}
  .logos .red{color:#a11d2b}
  .logos .blue{color:#1d4f91}
  .logos .dot{width:12px;height:12px;border-radius:50%}

  .footer{position:absolute;left:0;top:1100px;width:1152px;height:100px;background:var(--foot);border-top:1px solid #e2e2e2;font-family:"Open Sans",sans-serif;font-size:8.5px;color:var(--muted);text-align:center;padding-top:36px}
</style>
</head>
<body>

<div class="topbar">
  <div class="left">
    <span>SECURED &amp; UNSECURED BUSINESS LOANS</span>
    <svg width="9" height="9" viewBox="0 0 10 10"><circle cx="5" cy="5" r="4" fill="none" stroke="#fff" stroke-width="1"/><path d="M4 3l2 2-2 2" fill="none" stroke="#fff" stroke-width="1"/></svg>
    <span class="soft">WWW.CREDVISTA.IN</span>
  </div>
  <div class="right">
    <span>DO YOU HAVE ANY QUESTION?</span>
    <svg width="9" height="9" viewBox="0 0 10 10"><path d="M2 1l2 2-1 1.2c.6 1.2 1.6 2.2 2.8 2.8L7 6l2 2-1.2 1.2C4.5 9 1 5.5.8 2.2z" fill="#fff"/></svg>
    <span class="soft">CALL: 555 210 4417</span>
  </div>
</div>

<header class="header">
  <div class="brand"><span class="mark"></span>CredVista</div>
  <nav class="nav">
    <span>HOME</span><span>WHO WE ARE</span><span>SERVICES</span><span>BLOG</span><span>CAREER</span><span>REACH US</span>
  </nav>
</header>

<section class="hero" role="img" aria-label="Soft-focus bright office interior background">
  <div class="person" role="img" aria-label="Smiling businessman in a grey suit and striped tie"></div>
  <h1>LOOKING FOR<br>A SECURED OR<br>UNSECURED LOAN ?</h1>
  <div class="tag">WE WILL HELP YOU GET BEST INTEREST RATE</div>
  <div class="search">
    <div class="select">I would like to
      <svg width="8" height="5" viewBox="0 0 8 5"><path d="M.5.5l3.5 3.5L7.5.5" fill="none" stroke="#add136" stroke-width="1.2"/></svg></div>
    <div class="select">Select a Product
      <svg width="8" height="5" viewBox="0 0 8 5"><path d="M.5.5l3.5 3.5L7.5.5" fill="none" stroke="#add136" stroke-width="1.2"/></svg></div>
    <div class="btn-search">SEARCH
      <svg width="10" height="10" viewBox="0 0 10 10"><circle cx="4" cy="4" r="3" fill="none" stroke="#fff" stroke-width="1.6"/><path d="M6.3 6.3L9 9" stroke="#fff" stroke-width="1.8"/></svg></div>
  </div>
</section>

<section class="features">
  <h2 class="section-title">FEATURES</h2>
  <div class="cards">
    <div class="card active">
      <svg width="36" height="32" viewBox="0 0 36 32"><rect x="2" y="4" width="26" height="26" rx="3" fill="none" stroke="#0f2d52" stroke-width="3.5"/><path d="M8 15l7 7L33 3" fill="none" stroke="#0f2d52" stroke-width="5"/></svg>
      <p>Get Approval<br>within 7<br>business days</p>
    </div>
    <div class="card">
      <svg width="36" height="32" viewBox="0 0 36 32"><rect x="2" y="4" width="26" height="26" rx="3" fill="none" stroke="#cfcfcf" stroke-width="3.5"/><path d="M8 15l7 7L33 3" fill="none" stroke="#cfcfcf" stroke-width="5"/></svg>
      <p>Doorstep<br>Deliveries</p>
    </div>
    <div class="card">
      <svg width="36" height="32" viewBox="0 0 36 32"><rect x="2" y="4" width="26" height="26" rx="3" fill="none" stroke="#cfcfcf" stroke-width="3.5"/><path d="M8 15l7 7L33 3" fill="none" stroke="#cfcfcf" stroke-width="5"/></svg>
      <p>Easy<br>Documentation</p>
    </div>
    <div class="card">
      <svg width="36" height="32" viewBox="0 0 36 32"><rect x="2" y="4" width="26" height="26" rx="3" fill="none" stroke="#cfcfcf" stroke-width="3.5"/><path d="M8 15l7 7L33 3" fill="none" stroke="#cfcfcf" stroke-width="5"/></svg>
      <p>Compare Quote<br>from all major<br>financial institutions</p>
    </div>
  </div>
</section>

<section class="cta" role="img" aria-label="Dark blue toned photo of hands stacking coins beside a calculator">
  <h2>WHAT ARE YOU WAITING FOR?</h2>
  <div class="btn-inquire">INQUIRE NOW
    <svg width="11" height="11" viewBox="0 0 12 12"><circle cx="6" cy="6" r="5" fill="none" stroke="#fff" stroke-width="1.1"/><path d="M4.4 4.6a1.6 1.6 0 113 .6c-.5.6-1.4.8-1.4 1.8" fill="none" stroke="#fff" stroke-width="1.1"/><circle cx="6" cy="8.8" r=".7" fill="#fff"/></svg>
  </div>
</section>

<section class="partners">
  <h2 class="section-title">WE WORK WITH ALL PREMIUM FINANCIAL INSTITUTIONS</h2>
  <div class="logos">
    <span class="red">Northgate Bank</span>
    <span class="red">Meridian Bank</span>
    <span class="red">Harbor Trust Bank</span>
    <span class="blue"><i class="dot" style="background:#1d4f91"></i>Sterling Finserv</span>
    <span class="red"><i class="dot" style="background:#1d4f91"></i>Pinecrest</span>
  </div>
</section>

<footer class="footer">Copyright © 2016 CredVista. Privacy Policy</footer>

</body>
</html>
```